Bright Pelvic Health Business Card

Need a business card for a surgical practice called Bright Pelvic Health. We have recently selected a logo (attached). The business card will need to have two formats:
1) One with the logo/physician name/ contact info on the front and location information on the back.
2) One in "appointment reminder card" style with the logo/ contact info/ date/ time on the front and the location information on the back.

The front side should include the following information:
- Logo
- Rohan K. Desai, MD FACOG
- phone: 469-555-0172
- fax: 1-469-555-0188
- email: admin@brightpelvic.example
- website: www.brightpelvichealth.example

The back side should have the office locations listed:
4815 Juniper Way, Plano, TX 75093
3720 Baywood Rd, Plano, TX 75025
2245 Larkspur Ln, Irving, TX 75038
815 W Finch St S310, Dallas, TX 75201
3516 Quarry Blvd, Grand Prairie, TX 75051
6437 Wexley Crest Dr, San Antonio, TX 78240
5822 Ember Rd, Pasadena, TX 77504

Target Market(s)

1. Other physicians who might refer patients
2. Female patients

Industry/Entity Type

Business

Font styles to use
Other font styles liked:
• Tahoma for lettering

Requirements
Must have
• As per the instructions
Should not have
• No other images needed -- please try to keep font consistent with logo design. Can use Tahoma as the font for lettering.

```html
<!DOCTYPE html>
<html lang="en">
<head>
<meta charset="utf-8">
<title>Bright Pelvic Health – Business Card</title>
<link rel="stylesheet" href="https://fonts.googleapis.com/css2?family=Arimo&family=Montserrat:wght@500&display=swap">
<style>
  :root {
    --page: #ffffff;
    --card-blue: #2b4894;
    --card-glow: #f4f6fb;
    --glow-mid: #9fb0d6;
    --ink-light: #ffffff;
    --ink-label: #231f20;
    --brand-blue: #2d4f9e;
    --brand-red: #d9232a;
  }
  * { margin: 0; padding: 0; box-sizing: border-box; }
  html, body {
    width: 1200px; height: 639px; overflow: hidden;
    background: var(--page);
  }
  .sheet { position: relative; width: 1200px; height: 639px; }

  .side-label {
    position: absolute; top: 118px; width: 200px; text-align: center;
    font-family: "Arimo", Arial, sans-serif; font-size: 36px;
    color: var(--ink-label); line-height: 1;
  }
  .side-label--front { left: 208px; }
  .side-label--back { left: 822px; }

  .card {
    position: absolute; top: 168px; width: 558px; height: 338px;
    border-radius: 11px; overflow: hidden;
    background: var(--card-blue);
  }
  .card--front {
    left: 34px;
    background: radial-gradient(circle at 273px 165px, var(--card-glow) 0, var(--glow-mid) 110px, var(--card-blue) 260px);
  }
  .card--back {
    left: 614px;
    background: radial-gradient(circle at 283px 165px, var(--card-glow) 0, var(--glow-mid) 110px, var(--card-blue) 260px);
  }

  .silhouette {
    position: absolute; top: 0; height: 338px; width: 178px;
    background: var(--ink-light);
  }
  .card--front .silhouette {
    right: 0;
    border-radius: 90px 0 0 60px / 160px 0 0 120px;
  }
  .card--back .silhouette {
    left: 0;
    border-radius: 0 90px 60px 0 / 0 160px 120px 0;
  }

  .brand {
    position: absolute; top: 158px; width: 220px;
    display: flex; align-items: center; justify-content: center; gap: 7px;
    font-family: "Montserrat", Tahoma, sans-serif; font-weight: 500;
    font-size: 13px; letter-spacing: 0.08em; font-variant: small-caps;
    color: var(--brand-blue); white-space: nowrap;
  }
  .card--front .brand { left: 163px; }
  .card--back .brand { left: 173px; }
  .brand__dot {
    width: 10px; height: 10px; border-radius: 50%;
    background: var(--brand-red); flex: none;
  }

  .contact, .locations {
    position: absolute;
    font-family: "Montserrat", Tahoma, sans-serif; font-weight: 500;
    font-size: 12px; line-height: 16.8px; letter-spacing: 0.12em;
    font-variant: small-caps; color: var(--ink-light);
    list-style: none; white-space: nowrap;
  }
  .contact { left: 24px; top: 236px; }
  .contact .lower { text-transform: lowercase; }
  .locations { right: 22px; text-align: right; }
  .locations--upper { top: 18px; }
  .locations--lower { top: 266px; }
</style>
</head>
<body>
<main class="sheet">
  <h2 class="side-label side-label--front">front</h2>
  <h2 class="side-label side-label--back">back</h2>

  <section class="card card--front" aria-label="Card front">
    <div class="silhouette" role="img" aria-label="White butterfly-wing silhouette illustration"></div>
    <div class="brand"><span class="brand__dot"></span>Bright Pelvic Health</div>
    <ul class="contact">
      <li>Rohan K. Desai, MD FACOG</li>
      <li class="lower">phone: 469-555-0172</li>
      <li class="lower">fax:1-469-555-0188</li>
      <li class="lower">email: admin@brightpelvic.example</li>
      <li class="lower">website: www.brightpelvichealth.example</li>
    </ul>
  </section>

  <section class="card card--back" aria-label="Card back">
    <div class="silhouette" role="img" aria-label="White butterfly-wing silhouette illustration"></div>
    <div class="brand"><span class="brand__dot"></span>Bright Pelvic Health</div>
    <ul class="locations locations--upper">
      <li>4815 Juniper Way, Plano, TX 75093</li>
      <li>3720 Baywood Rd, Plano, TX 75025</li>
      <li>2245 Larkspur Ln, Irving, TX 75038</li>
      <li>815 W Finch St S310, Dallas, TX 75201</li>
    </ul>
    <ul class="locations locations--lower">
      <li>3516 Quarry Blvd, Grand Prairie, TX 75051</li>
      <li>6437 Wexley Crest Dr, San Antonio, TX 78240</li>
      <li>5822 Ember Rd, Pasadena, TX 77504</li>
    </ul>
  </section>
</main>
</body>
</html>
```